Loan Company looking to offer special summer loan rate for closed customers

We are wanting to design an A5 Summer Holiday themed leaflet. We would like to offer a 10% Cashback when re-opening their loan account.
The leaflet is aimed at our closed customers. We would like to use bright summer colours. I have uploaded one of our Christmas promotion leaflets for you to include the highlighted information to use in this new project. We have also uploaded some ideas of examples that we have seen online as rough guide.
"10% Cashback on all re-opened accounts in July and August 2023!"

```html
<!DOCTYPE html>
<html lang="en">
<head>
<meta charset="utf-8">
<title>Coral Financial Services – Summer Cashback Leaflet</title>
<link href="https://fonts.googleapis.com/css2?family=Outfit:wght@400;500;600;700;900&display=swap" rel="stylesheet">
<style>
  :root {
    --page-bg: #e4e4e4;
    --navy: #0d3566;
    --royal: #1d5cb3;
    --ink: #0b1a2a;
    --sky-top: #3fb3ec;
    --sky-mid: #7fd3f6;
    --sea: #49b8e6;
    --foam: #cdeefb;
    --sand: #f0b786;
    --sand-deep: #c8602a;
    --white: #ffffff;
  }
  * { margin: 0; padding: 0; box-sizing: border-box; }
  html, body {
    width: 1200px; height: 1200px; overflow: hidden;
    background: var(--page-bg);
    font-family: "Outfit", Arial, sans-serif;
  }
  .leaflet {
    position: absolute; left: 177px; top: 0;
    width: 846px; height: 1200px; overflow: hidden;
  }
  .beach-scene {
    position: absolute; inset: 0;
    background: linear-gradient(180deg,
      var(--sky-top) 0%, var(--sky-mid) 38%, var(--sea) 58%,
      var(--foam) 72%, var(--sea) 80%, var(--sand) 88%, var(--sand-deep) 100%);
  }
  .centered { position: absolute; left: 0; right: 0; text-align: center; }
  .brand-name {
    top: 150px; font-size: 84px; font-weight: 600; color: var(--navy);
    letter-spacing: 3px; line-height: 1;
  }
  .brand-line {
    top: 248px; font-size: 20px; font-weight: 600; color: var(--navy);
    letter-spacing: 3px;
  }
  .offer-lead { top: 322px; font-size: 25px; font-weight: 500; color: var(--ink); }
  .offer-headline {
    top: 346px; font-size: 72px; font-weight: 900; color: var(--royal);
    letter-spacing: -2px; line-height: 1.05;
    text-shadow: 0 3px 4px rgba(0,0,0,.3);
  }
  .offer-tail { top: 416px; font-size: 25px; font-weight: 500; color: var(--ink); }
  .example-box {
    position: absolute; left: 83px; width: 681px; top: 528px; height: 171px;
  }
  .example-frame {
    position: absolute; inset: 0; width: 681px; height: 171px; overflow: visible;
  }
  .example-frame path {
    fill: rgba(255,255,255,.12); stroke: var(--navy); stroke-width: 2;
  }
  .example-title {
    position: absolute; top: -16px; left: 50%; transform: translateX(-50%);
    padding: 0 10px; font-size: 27px; font-weight: 700; color: var(--navy);
    white-space: nowrap; border-left: 2px solid var(--navy); border-right: 2px solid var(--navy);
    line-height: 32px; height: 32px;
  }
  .example-line {
    position: absolute; left: 0; right: 0; text-align: center;
    font-size: 18px; color: var(--ink); text-transform: uppercase;
  }
  .example-line b { color: var(--navy); font-weight: 700; font-size: 20px; }
  .terms { font-size: 13.5px; font-weight: 600; color: var(--navy); line-height: 1.4; }
  .terms .dot { display: inline-block; width: 5px; height: 5px; background: var(--royal); margin: 0 5px 2px; }
  .prize-box {
    position: absolute; left: 136px; width: 573px; top: 831px; height: 84px;
    border: 2px solid rgba(255,255,255,.7); border-radius: 14px;
    background: rgba(40,110,170,.55);
    color: var(--white); font-size: 17px; line-height: 1.35; text-align: center;
    padding-top: 6px;
  }
  .prize-box b { font-weight: 700; }
  .contact-lead { top: 1022px; font-size: 20px; font-weight: 700; color: var(--navy); }
  .phone-number {
    top: 1040px; font-size: 80px; font-weight: 700; color: var(--white);
    -webkit-text-stroke: 3px var(--navy); paint-order: stroke fill;
    letter-spacing: -1px;
  }
</style>
</head>
<body>
  <main class="leaflet">
    <div class="beach-scene" role="img" aria-label="Tropical beach photo: blue sky with sun and gulls, palm leaves at the corners, breaking waves, and sand with a starfish and a beach ball"></div>

    <h1 class="centered brand-name">CORAL</h1>
    <p class="centered brand-line">FINANCIAL SERVICES (NORTHSHIRE) LIMITED</p>

    <p class="centered offer-lead">WE WOULD LIKE TO OFFER A</p>
    <p class="centered offer-headline">10% CASHBACK</p>
    <p class="centered offer-tail">WHEN RE-OPENING THEIR LOAN ACCOUNT.</p>

    <section class="example-box">
      <svg class="example-frame" viewBox="0 0 681 171" aria-hidden="true">
        <path d="M148 1 H13 Q1 1 1 13 V158 Q1 170 13 170 H668 Q680 170 680 158 V13 Q680 1 668 1 H533"/>
      </svg>
      <h2 class="example-title">REPRESENTATIVE EXAMPLE</h2>
      <p class="example-line" style="top:26px">Loan amount <b>£150.00</b> payable over <b>23 weeks</b> at <b>£10.50</b> per week.</p>
      <p class="example-line" style="top:62px">Interest is <b>£91.50</b>. The total amount payable is <b>£241.50</b>.</p>
      <p class="example-line" style="top:98px">Interest rate is <b>138.29%</b> per annum (fixed).</p>
      <p class="example-line" style="top:134px"><b>838.39%</b> APR representative.</p>
    </section>

    <p class="centered terms" style="top:772px">Terms and Conditions Apply <span class="dot"></span>All credit is subject to status &amp; affordability.<br><span class="dot"></span>Written quotations on request</p>

    <div class="prize-box">All customers that reopen their accounts with us before the<br><b>18th December</b> will be entered into our <b>free prize draw with<br>the chance to win a 15″ Nova Laptop</b></div>

    <p class="centered contact-lead">FOR MORE INFORMATION CONTACT OUR OFFICE ON</p>
    <p class="centered phone-number">01632 960 418</p>
  </main>
</body>
</html>
```